New Business Card Design Project

I would like a business card to match my truck wrap and logo. I would like the font to match my existing business card please.

Industry/Entity Type

Painter

Contact Information for Business Card

Rodrigo Venter 801-437-2910 Ventercoatings.utah@brushmail.net
SERVICES - Custom Paint & Stain, Interior & Exterior, Epoxy Coatings / Garage Floors, Cabinet Refinishing, Log Staining and Refinishing.

Requirements
Nice to have
• I would like to have the white and grey line like the bottom of my vehicle wrap, Light Grey to match my truck also.

```html
<!DOCTYPE html>
<html lang="en">
<head>
<meta charset="utf-8">
<title>Venter Coatings – Business Card</title>
<link rel="stylesheet" href="https://fonts.googleapis.com/css2?family=Krona+One&family=Michroma&display=swap">
<style>
  :root {
    --stage: #000000;
    --card-white: #ffffff;
    --truck-grey: #c4cad2;
    --brand-blue: #1a9ee0;
    --text-light: #ffffff;
  }
  * { margin: 0; padding: 0; box-sizing: border-box; }
  html, body {
    width: 1200px;
    height: 1000px;
    overflow: hidden;
    background: var(--stage);
  }
  .card {
    position: absolute;
    left: 128px;
    top: 205px;
    width: 945px;
    height: 591px;
    background: var(--card-white);
    overflow: hidden;
    font-family: "Michroma", sans-serif;
  }
  .card-bands {
    position: absolute;
    inset: 0;
  }
  .brand {
    position: absolute;
    left: 40px;
    top: 72px;
    display: flex;
    align-items: center;
    gap: 18px;
  }
  .brand-square {
    width: 44px;
    height: 44px;
    background: var(--brand-blue);
    flex: none;
  }
  .brand-name {
    font-family: "Krona One", sans-serif;
    color: var(--brand-blue);
    font-size: 30px;
    line-height: 1.25;
    letter-spacing: 1px;
  }
  .phone {
    position: absolute;
    right: 20px;
    top: 30px;
    font-family: "Krona One", sans-serif;
    color: var(--brand-blue);
    font-size: 25px;
    letter-spacing: 4px;
  }
  .contact {
    position: absolute;
    left: 38px;
    top: 364px;
    color: var(--text-light);
  }
  .contact-name {
    font-family: "Krona One", sans-serif;
    font-size: 28px;
    letter-spacing: 1px;
    line-height: 1.2;
  }
  .contact-email {
    font-size: 19px;
    margin-top: 6px;
  }
  .services {
    position: absolute;
    left: 553px;
    top: 298px;
    width: 380px;
    color: var(--text-light);
    font-size: 19.5px;
    line-height: 30px;
  }
  .services-title {
    font-family: "Krona One", sans-serif;
    font-size: 21px;
  }
</style>
</head>
<body>
  <div class="card">
    <svg class="card-bands" width="945" height="591" viewBox="0 0 945 591" aria-hidden="true">
      <polygon points="0,215 465,215 597,87 945,87 945,591 0,591" fill="var(--truck-grey)"/>
      <polyline points="0,231 471,231 603,101 945,101" fill="none" stroke="var(--card-white)" stroke-width="12" stroke-linejoin="miter"/>
    </svg>

    <div class="brand">
      <div class="brand-square"></div>
      <div class="brand-name">VENTER<br>COATINGS</div>
    </div>

    <div class="phone">801.437.2910</div>

    <div class="contact">
      <div class="contact-name">RODRIGO VENTER</div>
      <div class="contact-email">ventercoatings.utah@brushmail.net</div>
    </div>

    <div class="services">
      <div class="services-title">SERVICES</div>
      Custom Paint &amp; Stain,<br>
      Interior &amp; Exterior, Epoxy<br>
      Coatings/Garage Floors,<br>
      Cabinet Refinishing,<br>
      Log Staining and<br>
      Refinishing.
    </div>
  </div>
</body>
</html>
```